Menu Design Project

Bo velle hair and beauty service menu
we need a menu to display a handful of our services to give our customers an idea of our pricing

Cutting
Ladies cuts from $35
Men's cuts from $25
All cuts are included with a wash and dry off

Quorvel colours
All over colours start from $55
price will vary depending upon length and thickness of hair

Foiling
starts from $50
Price will vary depending upon length of hair

Toners
from $30

Blowdries
from $35

Upstyling
wedding styling from $45
Please enquire for special occasion styling also

Beauty Services

Waxing
Eyebrow wax and shape $17.50
Lip $10
Chin/sides $20
Legs from $25
Bikini $20
XX $30
XXX $45
Back from $25
Chest from $25

Eyes
Eyebrow tinting $15
Eyelash tinting $20
Eyelash extensions from $90

Sandrift facials
Express facial $45
Deluxe facial $95

Acrylic nails
full set $60
Gel polish $35
Manicures from $35
Pedicures from $45

can provide logo and other images to help

Industry/Entity Type

Hair

Requirements
Must have
• must be called a service menu
must be eye catching and memorable but not excessive
Nice to have
• postcard style size hair menu on one side
beauty menu on the other side
elegant classy design
Should not have
• must not be called a price list
stay away from traditional price list style in terms of folding out leaflet

```html
<!DOCTYPE html>
<html lang="en">
<head>
<meta charset="utf-8">
<title>Bo velle — Beauty Services</title>
<link rel="stylesheet" href="https://fonts.googleapis.com/css2?family=Inter:wght@200;300;400&display=swap">
<style>
  :root {
    --paper: #eef1f4;
    --paper-light: #f8f9fa;
    --ink: #111111;
    --ink-soft: #4a4a4a;
    --price: #222222;
    --skin-light: #ecd9d0;
    --skin-mid: #dcbfb2;
    --skin-shadow: #c9a898;
    --hair: #3a2e2a;
  }
  * { margin: 0; padding: 0; box-sizing: border-box; }
  html, body { width: 1200px; height: 866px; overflow: hidden; }
  body {
    font-family: "Inter", "Helvetica Neue", Arial, sans-serif;
    background: linear-gradient(100deg, var(--paper) 0%, var(--paper-light) 45%, #ffffff 60%);
    position: relative;
    color: var(--ink);
  }
  .portrait {
    position: absolute;
    left: 440px; top: 0;
    width: 760px; height: 866px;
    background:
      radial-gradient(ellipse 260px 300px at 92% 8%, var(--hair) 0%, rgba(58,46,42,0.6) 45%, rgba(58,46,42,0) 100%),
      radial-gradient(ellipse 420px 520px at 60% 55%, var(--skin-light) 0%, var(--skin-mid) 55%, var(--skin-shadow) 80%, rgba(201,168,152,0) 100%),
      linear-gradient(180deg, #e9e6e6 0%, #efe8e6 100%);
    -webkit-mask-image: linear-gradient(90deg, transparent 0%, #000 30%);
            mask-image: linear-gradient(90deg, transparent 0%, #000 30%);
  }
  .section-title {
    position: absolute;
    left: 110px; top: 590px;
    transform: translate(-50%, -50%) rotate(-90deg);
    font-size: 46px;
    font-weight: 200;
    color: var(--ink-soft);
    white-space: nowrap;
    letter-spacing: 0.5px;
  }
  .service-group {
    position: absolute;
    left: 165px;
    width: 360px;
  }
  .service-group h2 {
    font-size: 21px;
    font-weight: 400;
    line-height: 28px;
    color: var(--ink);
  }
  .service-list { list-style: none; }
  .service-list li {
    display: grid;
    grid-template-columns: 297px auto;
    align-items: center;
    height: 28px;
  }
  .service-name {
    font-size: 22px;
    font-weight: 200;
    color: var(--ink-soft);
    white-space: nowrap;
  }
  .service-price {
    font-size: 13px;
    font-weight: 400;
    color: var(--price);
  }
  .group-waxing { top: 85px; }
  .group-eyes { top: 394px; }
  .group-facials { top: 534px; }
  .group-nails { top: 647px; }
  .brand {
    position: absolute;
    left: 735px; top: 490px;
  }
  .brand-name {
    font-size: 66px;
    font-weight: 400;
    color: var(--ink);
    line-height: 1;
    letter-spacing: 1px;
  }
  .brand-tagline {
    margin-top: 20px;
    margin-left: 20px;
    font-size: 26px;
    font-weight: 200;
    color: var(--ink-soft);
  }
</style>
</head>
<body>
  <div class="portrait" role="img" aria-label="Soft-focus photograph of a relaxed woman in profile with closed eyes"></div>

  <h1 class="section-title">Beauty Services</h1>

  <section class="service-group group-waxing">
    <h2>Waxing</h2>
    <ul class="service-list">
      <li><span class="service-name">Eyebrow wax and shape</span><span class="service-price">$17.50</span></li>
      <li><span class="service-name">Lip</span><span class="service-price">$10</span></li>
      <li><span class="service-name">Chin/sides</span><span class="service-price">$20</span></li>
      <li><span class="service-name">Legs from</span><span class="service-price">$25</span></li>
      <li><span class="service-name">Bikini</span><span class="service-price">$20</span></li>
      <li><span class="service-name">XX</span><span class="service-price">$30</span></li>
      <li><span class="service-name">XXX</span><span class="service-price">$45</span></li>
      <li><span class="service-name">Back from</span><span class="service-price">$25</span></li>
      <li><span class="service-name">Chest from</span><span class="service-price">$25</span></li>
    </ul>
  </section>

  <section class="service-group group-eyes">
    <h2>Eyes</h2>
    <ul class="service-list">
      <li><span class="service-name">Eyebrow tinting</span><span class="service-price">$15</span></li>
      <li><span class="service-name">Eyelash tinting</span><span class="service-price">$20</span></li>
      <li><span class="service-name">Eyelash extensions from</span><span class="service-price">$90</span></li>
    </ul>
  </section>

  <section class="service-group group-facials">
    <h2>Sandrift facials</h2>
    <ul class="service-list">
      <li><span class="service-name">Express facial</span><span class="service-price">$45</span></li>
      <li><span class="service-name">Deluxe facial</span><span class="service-price">$95</span></li>
    </ul>
  </section>

  <section class="service-group group-nails">
    <h2>Acrylic nails</h2>
    <ul class="service-list">
      <li><span class="service-name">full set</span><span class="service-price">$60</span></li>
      <li><span class="service-name">Gel polish</span><span class="service-price">$35</span></li>
      <li><span class="service-name">Manicures from</span><span class="service-price">$35</span></li>
      <li><span class="service-name">Pedicures from</span><span class="service-price">$45</span></li>
    </ul>
  </section>

  <div class="brand">
    <div class="brand-name">Bo velle</div>
    <div class="brand-tagline">Service menu</div>
  </div>
</body>
</html>
```